Professional Modern Website Design

We are a premium IT services provider to the financial industry based in London. Our company is called Velmar our current holding page is www.velmar.co.uk. We require a new website to match our new corporate identity. This project is for the design phase only. Development will be handled in-house. I have attached examples of wire frames we have developed (although open to suggestions for improvement) Our brand document that should demonstrate current brand, inc how we communicate to potential clients and finally mostly completed web-content.
We are looking for designers that can create something that sets us apart from our competitors.
Target Market(s)
IT Decision makers in Finance companies such as; hedge funds, private investment banks etc
Industry/Entity Type
Financial
Number of Pages Required
5+ page
Requirements
Must have
- hexagon elements in the design, unique design.
Nice to have
- Blog and social media feeds
Should not have
- Should not resemble a downloaded template

```html
<!DOCTYPE html>
<html lang="en">
<head>
<meta charset="utf-8">
<title>Velmar – IT Services for Finance</title>
<link rel="stylesheet" href="https://fonts.googleapis.com/css2?family=Dosis:wght@400;500&family=Open+Sans:wght@400;600;700&display=swap">
<style>
:root{
  --orange:#f5841f;
  --orange-hot:#f26a2a;
  --ink:#161616;
  --ink-deep:#0b0b0b;
  --panel:#3b3b3b;
  --white:#ffffff;
  --text:#222222;
  --btn-dark:#3d3d3d;
}
*{box-sizing:border-box;margin:0;padding:0}
html,body{width:826px;height:1200px;overflow:hidden;background:var(--ink)}
body{position:relative;font-family:"Open Sans",sans-serif;color:var(--white)}
.abs{position:absolute}

/* hero */
.hero{left:0;top:0;width:826px;height:426px;overflow:hidden}
.hero-photo{position:absolute;inset:0}
.brand-panel{left:0;top:0;width:82px;height:123px;background:var(--panel);display:flex;flex-direction:column;align-items:center;justify-content:center;gap:8px}
.brand-panel .mark{width:30px;height:30px;background:var(--orange)}
.brand-panel .name{font-family:"Dosis",sans-serif;font-size:11px;letter-spacing:3px;color:#d8d8d8}
.main-nav{left:129px;top:55px;display:flex;gap:19px;font-family:"Dosis",sans-serif;font-size:11px;letter-spacing:.5px}
.main-nav .active{color:var(--orange)}
.dropdown{left:179px;top:80px;width:158px;height:132px;background:var(--white);color:var(--text);font-size:7.6px;padding:20px 10px 0 17px;line-height:1.2}
.dropdown li{list-style:none;margin-bottom:10px}
.dropdown li:first-child{color:var(--orange);margin-bottom:6px}
.dropdown-caret{left:193px;top:80px;width:0;height:0;border-left:6px solid transparent;border-right:6px solid transparent;border-top:6px solid var(--orange)}
.social{left:734px;top:53px;display:flex;gap:1px}
.hero-title{left:129px;top:183px;font-family:"Dosis",sans-serif;font-size:21px;line-height:25px;font-weight:400;z-index:0}
.hero-title span{display:block;padding-left:4px}
.hero-copy{left:129px;top:241px;width:350px;font-size:10.4px;line-height:12.4px;color:#eeeeee}
.hero-copy b{font-weight:400;color:var(--orange)}
.btn-hero{left:129px;top:302px;width:102px;height:26px;background:var(--orange-hot);font-family:"Dosis",sans-serif;font-size:13px;letter-spacing:.5px;display:flex;align-items:center;justify-content:center}
.slider-dots{left:762px;top:378px;display:flex;gap:2px}
.slider-dots i{width:8px;height:8px;border:1.2px solid var(--white);border-radius:50%}
.slider-dots i.on{background:var(--white)}
.dropdown,.dropdown-caret{z-index:2}

/* audience */
.audience{left:0;top:426px;width:826px;height:521px;background:radial-gradient(ellipse at 50% 30%,#262626 0%,var(--ink) 60%,var(--ink-deep) 100%)}
.audience-mark{left:406px;top:464px;width:14px;height:14px;background:var(--orange)}
.audience-title{left:0;top:497px;width:826px;text-align:center;font-family:"Dosis",sans-serif;font-size:24px;font-weight:400}
.audience-lead{left:160px;top:531px;width:506px;text-align:center;font-size:10.4px;line-height:12.6px}
.card{width:328px;height:153px;background:var(--white);color:var(--text);overflow:hidden}
.card svg{position:absolute;left:0;top:0}
.card-body{position:absolute;width:170px}
.card-title{font-size:12px;font-weight:700;color:var(--orange);margin-bottom:10px}
.card-text{font-size:8.2px;line-height:9.8px;margin-bottom:10px}
.btn-card{display:inline-block;background:var(--btn-dark);color:var(--white);font-size:6.6px;padding:4px 7px}

/* footer */
.footer{left:0;top:947px;width:826px;height:220px;background:var(--orange)}
.footer-brand{left:82px;top:1028px;font-family:"Dosis",sans-serif;font-size:16px;font-weight:500;letter-spacing:2px}
.footer-links{top:1002px;list-style:none;font-size:9px;line-height:15.4px}
.footer-links li::before{content:"›";margin-right:4px}
.field{border:1px solid var(--white);font-size:8px;padding:8px 12px;letter-spacing:.3px}
.btn-send{left:391px;top:1095px;width:83px;height:28px;border:1px solid var(--white);font-family:"Dosis",sans-serif;font-size:13px;display:flex;align-items:center;justify-content:center}
.legal{left:0;top:1167px;width:826px;height:33px;background:var(--ink-deep);font-size:8.4px;display:flex;align-items:center;justify-content:center;color:#e8e8e8}
</style>
</head>
<body>

<header class="hero abs">
  <svg class="hero-photo" width="826" height="426" role="img" aria-label="Black and white aerial photo of a city skyline by the river at dusk">
    <defs>
      <linearGradient id="sky" x1="0" y1="0" x2="0" y2="1">
        <stop offset="0" stop-color="#2a2a2a"/><stop offset=".45" stop-color="#5a5a5a"/><stop offset=".7" stop-color="#3a3a3a"/><stop offset="1" stop-color="#1b1b1b"/>
      </linearGradient>
      <radialGradient id="glow" cx=".7" cy=".55" r=".5">
        <stop offset="0" stop-color="#8a8a8a" stop-opacity=".5"/><stop offset="1" stop-color="#8a8a8a" stop-opacity="0"/>
      </radialGradient>
    </defs>
    <rect width="826" height="426" fill="url(#sky)"/>
    <rect width="826" height="426" fill="url(#glow)"/>
  </svg>
  <div class="brand-panel abs"><span class="mark"></span><span class="name">VELMAR</span></div>
  <nav class="main-nav abs"><span>ABOUT</span><span class="active">SERVICES</span><span>PARTNER</span><span>CLIENTS</span><span>CONTACT</span></nav>
  <h1 class="hero-title abs">YOU NEVER SEE US, WE'RE INVISIBLE<span>BUT ALWAYS SUPPORTING YOU.</span></h1>
  <div class="dropdown-caret abs"></div>
  <ul class="dropdown abs">
    <li>Data Center &amp; Infrastructure</li>
    <li>Support, Managed &amp; Professional Services</li>
    <li>Voice and Data</li>
    <li>Hosting and Cloud</li>
    <li>Security and IRM</li>
  </ul>
  <div class="social abs">
    <svg width="66" height="18" aria-label="Social links">
      <polygon points="8,0 16,4.5 16,13.5 8,18 0,13.5 0,4.5" fill="var(--orange)"/>
      <polygon points="25,.5 32.5,4.7 32.5,13.3 25,17.5 17.5,13.3 17.5,4.7" fill="none" stroke="#fff"/>
      <polygon points="41.5,.5 49,4.7 49,13.3 41.5,17.5 34,13.3 34,4.7" fill="none" stroke="#fff"/>
      <polygon points="58,.5 65.5,4.7 65.5,13.3 58,17.5 50.5,13.3 50.5,4.7" fill="none" stroke="#fff"/>
    </svg>
  </div>
  <p class="hero-copy abs"><b>Velmar</b> is one of the leading systems integrators to the world's finance sector. We are an extension of your business and our services portfolio has been built so you always have access to a complete partner.</p>
  <div class="btn-hero abs">LEARN MORE</div>
  <div class="slider-dots abs"><i></i><i class="on"></i><i></i><i></i></div>
</header>

<section class="audience abs"></section>
<div class="audience-mark abs"></div>
<h2 class="audience-title abs">Who we are ?</h2>
<p class="audience-lead abs">If you're working a financial organisation, we have the servies to help everyone in your organisation work more efficiently, productively and profitably.</p>

<article class="card abs" style="left:82px;top:584px">
  <svg width="328" height="153" role="img" aria-label="Photo of two business partners shaking hands outside office towers"><polygon points="0,0 128,0 133,76 90,153 0,153" fill="#8f9398"/></svg>
  <div class="card-body" style="left:151px;top:41px"><h3 class="card-title">Hedgefund Partner/CEO</h3><p class="card-text">Lorem ipsum dolor sit amet, consectetur adipisicing elit, sed do eiusmod incididunt ut labore et dolore magna.</p><span class="btn-card">LEARN MORE</span></div>
</article>
<article class="card abs" style="left:415px;top:584px">
  <svg width="328" height="153" role="img" aria-label="Portrait photo of a senior finance executive in a suit"><polygon points="0,0 110,0 150,76 110,153 0,153" fill="#a3a8ae"/></svg>
  <div class="card-body" style="left:148px;top:41px"><h3 class="card-title">CFO</h3><p class="card-text">Lorem ipsum dolor sit amet, consectetur adipisicing elit, sed do eiusmod incididunt ut labore et dolore magna.</p><span class="btn-card">LEARN MORE</span></div>
</article>
<article class="card abs" style="left:82px;top:743px">
  <svg width="328" height="153" role="img" aria-label="Portrait photo of a technology executive in a brown suit"><polygon points="328,0 269,0 196,76 239,153 328,153" fill="#6e6660"/></svg>
  <div class="card-body" style="left:21px;top:41px"><h3 class="card-title">CTO</h3><p class="card-text">Lorem ipsum dolor sit amet, consectetur adipisicing elit, sed do eiusmod incididunt ut labore et dolore magna.</p><span class="btn-card">LEARN MORE</span></div>
</article>
<article class="card abs" style="left:415px;top:743px">
  <svg width="328" height="153" role="img" aria-label="Photo of a team of employees working together in a bright office"><polygon points="328,0 240,0 197,76 240,153 328,153" fill="#b9bcbf"/></svg>
  <div class="card-body" style="left:21px;top:46px"><h3 class="card-title">Employee</h3><p class="card-text">Lorem ipsum dolor sit amet, consectetur adipisicing elit, sed do eiusmod incididunt ut labore et dolore magna.</p><span class="btn-card">LEARN MORE</span></div>
</article>

<footer class="footer abs"></footer>
<div class="footer-brand abs">VELMAR</div>
<ul class="footer-links abs" style="left:186px"><li>Home</li><li>About</li><li>Services</li><li>Partners</li><li>Clients</li><li>Contacts</li></ul>
<ul class="footer-links abs" style="left:269px"><li>Facepage</li><li>Chirper</li><li>Circles Plus</li><li>Linkline</li></ul>
<div class="field abs" style="left:391px;top:1004px;width:174px;height:28px">User</div>
<div class="field abs" style="left:569px;top:1004px;width:173px;height:28px">Email</div>
<div class="field abs" style="left:391px;top:1038px;width:351px;height:53px">Comments</div>
<div class="btn-send abs">Send</div>
<div class="legal abs">© Copyright © 2015, Velmar Inc. All Rights Reserved</div>

</body>
</html>
```